Letterhead design for ZENTORA company

I need an A4 letterhead design for my company "Zentora Electrical Products". I need the letterhead to match my current logo and business card designs. I would like it to be colourful and match the design of the business card in terms of the flowing line of colour where the information is.  

Target Market(s)

Adults aged 20 - 50 Upper middle class.

Industry/Entity Type

It Company

Requirements
Must have
• Must be A4 size and match my current logo and business card designs. Must be clean simple and eye catching.

• Must have the following information

• Zentora Electrical Products LTD
• 7 Ardley Close
• Chiswick
• London
• England
• W9 3QX
• Company No. 05316429
• VAT No. GB 627150384

• Telephone: 02081594360
• Mobile: 07815062247
• Email: info@zentora-goods.co.uk
Nice to have
• nice to have a wave of colour like the business card.
Should not have
• Should not be a different colour scheme to the business card and logo design.

```html
<!DOCTYPE html>
<html lang="en">
<head>
<meta charset="utf-8">
<title>Zentora Electrical Products – Letterhead</title>
<link href="https://fonts.googleapis.com/css2?family=Questrial&family=Open+Sans:wght@400&family=Carlito&display=swap" rel="stylesheet">
<style>
  :root {
    --teal-deep: #1a93a0;
    --teal-mid: #3cc7c6;
    --teal-bright: #62ffea;
    --aqua-line: #8ffbff;
    --grey-light: #f4f4f4;
    --grey-mid: #d6d6d6;
    --paper: #ffffff;
    --ink-light: #ffffff;
  }
  html, body {
    margin: 0;
    padding: 0;
    width: 851px;
    height: 1200px;
    overflow: hidden;
    background: var(--paper);
  }
  .letterhead {
    position: relative;
    width: 851px;
    height: 1200px;
    background: var(--paper);
    overflow: hidden;
  }
  .wave-art {
    position: absolute;
    inset: 0;
    width: 851px;
    height: 1200px;
  }
  .brand {
    position: absolute;
    top: 10px;
    left: 620px;
    width: 212px;
    color: var(--ink-light);
    font-family: "Questrial", sans-serif;
    font-weight: 400;
    text-align: left;
    white-space: nowrap;
  }
  .brand-name {
    display: block;
    font-size: 43px;
    line-height: 52px;
    letter-spacing: 0;
  }
  .brand-tagline {
    display: block;
    font-size: 20px;
    line-height: 24px;
    letter-spacing: 1.4px;
    margin-top: 6px;
  }
  .contact {
    position: absolute;
    left: 78px;
    top: 1096px;
    width: 300px;
    text-align: center;
    color: var(--ink-light);
    font-family: "Open Sans", sans-serif;
    font-size: 10.5px;
    letter-spacing: 0.8px;
    line-height: 15.2px;
  }
  .contact p { margin: 0; white-space: nowrap; }
  .contact .registration {
    font-family: "Carlito", sans-serif;
    font-size: 10.5px;
    letter-spacing: 0;
    margin-top: 1px;
  }
  .registration .gap { display: inline-block; width: 18px; }
</style>
</head>
<body>
<main class="letterhead">
  <svg class="wave-art" viewBox="0 0 851 1200" xmlns="http://www.w3.org/2000/svg" aria-hidden="true">
    <defs>
      <linearGradient id="greySweep" x1="0" y1="0" x2="1" y2="0">
        <stop offset="0" stop-color="var(--grey-light)"/>
        <stop offset="0.4" stop-color="#fafafa"/>
        <stop offset="1" stop-color="var(--grey-mid)"/>
      </linearGradient>
      <radialGradient id="tealGlowTop" cx="0.5" cy="0.45" r="0.6">
        <stop offset="0" stop-color="var(--teal-bright)"/>
        <stop offset="0.55" stop-color="var(--teal-mid)"/>
        <stop offset="1" stop-color="var(--teal-deep)"/>
      </radialGradient>
      <linearGradient id="tealCorner" x1="0" y1="0" x2="1" y2="1">
        <stop offset="0" stop-color="var(--teal-mid)"/>
        <stop offset="1" stop-color="var(--teal-bright)"/>
      </linearGradient>
      <radialGradient id="tealGlowFoot" cx="0.5" cy="0.4" r="0.65">
        <stop offset="0" stop-color="var(--teal-bright)"/>
        <stop offset="0.6" stop-color="var(--teal-mid)"/>
        <stop offset="1" stop-color="var(--teal-deep)"/>
      </radialGradient>
    </defs>

    <path class="header-grey" d="M0,0 C200,110 470,162 630,160 C740,159 815,147 851,136 V0 Z" fill="url(#greySweep)"/>
    <path class="header-corner" d="M0,0 C110,68 230,108 342,130 C230,140 100,139 0,133 Z" fill="url(#tealCorner)"/>
    <path class="header-main" d="M65,0 C260,95 520,128 660,128 C760,128 825,120 851,109 V0 Z" fill="url(#tealGlowTop)"/>
    <path class="header-inner" d="M65,0 C260,85 520,108 660,106 C760,104 825,96 851,88 V0 Z" fill="url(#tealGlowTop)" opacity="0.9"/>
    <path class="header-line" d="M65,0 C260,85 520,108 660,106 C760,104 825,96 851,88" fill="none" stroke="var(--aqua-line)" stroke-width="2.5"/>
    <path class="header-edge" d="M0,0 C110,68 230,108 342,130" fill="none" stroke="#ffffff" stroke-width="1.5" opacity="0.8"/>

    <path class="footer-grey" d="M340,1084 C500,1062 700,1050 851,1081 V1200 H340 Z" fill="url(#greySweep)"/>
    <path class="footer-main" d="M0,1083 C180,1074 560,1092 851,1170 V1200 H0 Z" fill="url(#tealGlowFoot)"/>
  </svg>

  <header class="brand">
    <span class="brand-name">ZENTORA</span>
    <span class="brand-tagline">Electrical Products</span>
  </header>

  <footer class="contact">
    <p>7 Ardley Close, Chiswick, London, England, W9 3QX</p>
    <p>02081594360</p>
    <p>07815062247</p>
    <p>info@zentora-goods.co.uk</p>
    <p>www.zentora-goods.co.uk</p>
    <p class="registration">Company No. 05316429<span class="gap"></span>VAT No. GB 627150384</p>
  </footer>
</main>
</body>
</html>
```